Corporate Breakfast Flyer - Breakfast Talk (One Page)

Create a flyer with below using your own selection of content and images from the below. You do not have to use all images I have left them all there for your choice. Please use blue type colors like in our logo. Should be a corporate and professional feel to it.

Venue: Brindlemere Links Club 17 Carrowvale St, Oatlands NSW 2117
Date: Thursday the 22nd of September 2016
7.30am: Breakfast and networking
8.00am: Dylan Morrow speaking – Leadership and Motivation
9.00am: Business Card draw and finish

• Mini croissants on arrival – Ham & cheese, tomato & cheese, plain
• Toast station – assorted sliced breads & spreads
• Banana bread slice with honey ricotta
• Chicken & herb chipolata
• Marinated lamb chops
• Creamy scrambled eggs with chives
• Mushroom & cherry tomato kebabs
• Hash browns
• Assorted fruit cocktails with yoghurt & granola, juice station
• Tea and coffee station included
Topic: Leadership and Motivation
Speaker profile (Dylan Morrow):
Dylan Morrow is a four-time Meridian Cup competitor, winning basketball player, coach, entrepreneur, motivational speaker, brand ambassador - and one of Australia's most recognized personalities and sporting figures.
He was the first-ever Australian player to be signed to the PCX from the QVR and he also captained the Harbour Falcons to their first-ever title, helping to raise the profile of basketball around Australia. He has represented Australia at four Meridian Cup and played professionally for more than 20 years in Australia, Europe and the PCX. In February 2012 he was appointed Head Coach of the Harbour Falcons.
Following his retirement from playing, Dylan earned a reputation as a successful entrepreneur and businessman. He built up a successful business in fast food franchising with more than 30 stores across six different brands which, at its peak in 2010, employed over 350 people. After his company was severely affected by the collapse of an KTE listed company in which he had purchased a 10-year contract, Dylan had to start all over again.
Dylan has also held hosting, commentary and columnist roles with WMR, Vista Seven, Orbit Broadcast and Pike Athletics.

Target Market(s)

Finance leaders, Finance Directors, Controllers and CFO's

Font styles to use
Serif
Sans Serif

Colors
33a6d7
0592cd
0355a3
3276b5
85abd2
85cae6

Requirements
Must have
• Must be one page A4 will be sent electronically
Nice to have
• Any other images you feel may be pertinant, I have attached lots of images for you to use for this project please do not use to many. I have attached more so you have more selection
Should not have
• All Images

```html
<!DOCTYPE html>
<html lang="en">
<head>
<meta charset="utf-8">
<title>Corporate Breakfast – Leadership &amp; Motivation</title>
<link href="https://fonts.googleapis.com/css2?family=Bebas+Neue&family=Great+Vibes&family=Montserrat:wght@400;500&display=swap" rel="stylesheet">
<style>
  :root {
    --navy: #0b2f78;
    --royal: #0355a3;
    --mid: #3276b5;
    --sky: #85abd2;
    --pale: #85cae6;
    --white: #ffffff;
    --header-a: #9fb3b8;
    --header-b: #5f7c86;
    --panel: rgba(16, 36, 110, 0.72);
    --panel-line: rgba(255, 255, 255, 0.85);
  }
  * { box-sizing: border-box; margin: 0; padding: 0; }
  html, body { width: 849px; height: 1200px; overflow: hidden; background: var(--navy); }
  .flyer {
    position: relative; width: 849px; height: 1200px; overflow: hidden;
    font-family: "Montserrat", sans-serif; color: var(--white);
    background: linear-gradient(180deg, #1a4fa3 0%, #1f5db4 45%, #3a78c4 78%, #6d9fd6 100%);
  }
  .backdrop {
    position: absolute; left: 0; top: 115px; width: 849px; height: 1085px;
    background:
      radial-gradient(ellipse 260px 360px at 360px 330px, rgba(150,180,230,0.35), transparent 70%),
      radial-gradient(ellipse 500px 180px at 430px 1080px, rgba(200,220,245,0.35), transparent 70%);
  }
  .masthead {
    position: absolute; left: 0; top: 0; width: 849px; height: 115px;
    background: linear-gradient(180deg, var(--header-a), var(--header-b));
  }
  .masthead__title {
    position: absolute; left: 36px; top: 18px;
    font-family: "Great Vibes", cursive; font-weight: 400; font-size: 62px; line-height: 1; color: var(--white);
  }
  .host { position: absolute; right: 42px; top: 30px; display: flex; align-items: center; gap: 10px; }
  .host__dot { width: 46px; height: 46px; border-radius: 50%; background: var(--white); }
  .host__text { text-align: right; }
  .host__label { font-family: "Bebas Neue", sans-serif; font-size: 15px; line-height: 1; }
  .host__name { font-family: "Montserrat", sans-serif; font-weight: 500; font-size: 31px; line-height: 1.05; }

  .speaker { position: absolute; left: 42px; top: 132px; font-family: "Bebas Neue", sans-serif; }
  .speaker__with { font-size: 21px; line-height: 1; }
  .speaker__name { font-size: 124px; line-height: 100px; margin-top: 12px; }

  .topic { position: absolute; right: 40px; top: 150px; text-align: right; font-family: "Bebas Neue", sans-serif; }
  .topic__title { font-weight: 400; font-size: 94px; line-height: 74px; }
  .topic__date { font-size: 44px; line-height: 1; margin-top: 22px; }

  .portrait {
    position: absolute; left: 41px; top: 383px; width: 230px; height: 230px;
    border: 2px solid var(--white);
    background: radial-gradient(circle at 55% 45%, #c9a58c 0%, #8a6654 40%, #2a1c18 100%);
  }
  .panel {
    position: absolute; background: var(--panel); border: 1px solid var(--panel-line);
    font-size: 12.6px; line-height: 20px; color: #e6ecf7;
  }
  .panel p + p { margin-top: 20px; }
  .panel--bio { left: 300px; top: 383px; width: 510px; height: 230px; padding: 17px 18px; }
  .panel--career { left: 41px; top: 630px; width: 769px; height: 164px; padding: 14px 22px; font-size: 12.2px; line-height: 19px; }
  .panel--career p + p { margin-top: 19px; }

  .schedule__slot {
    position: absolute; left: 41px; width: 243px; padding: 12px 18px;
    background: var(--panel); border: 1px solid var(--panel-line);
    text-align: right; font-size: 16.5px; line-height: 24px;
  }
  .menu { position: absolute; left: 323px; top: 802px; list-style: none; font-size: 14.6px; line-height: 24.4px; }
  .menu li::before { content: "•"; margin-right: 8px; }

  .venue-tag {
    position: absolute; left: 458px; top: 1065px; width: 185px; height: 56px;
    background: var(--panel); border: 1px solid var(--panel-line);
    font-family: "Bebas Neue", sans-serif; font-size: 44px; line-height: 56px; text-align: right; padding-right: 12px;
  }
  .venue-mark {
    position: absolute; left: 655px; top: 1044px; width: 154px; height: 114px;
    background: rgba(210, 225, 240, 0.45);
    display: flex; align-items: center; justify-content: center; gap: 8px;
  }
  .venue-mark__dot { width: 14px; height: 14px; border-radius: 50%; background: var(--white); }
  .venue-mark__name { font-family: "Montserrat", sans-serif; font-size: 11px; line-height: 14px; width: 100px; }
  .address {
    position: absolute; left: 42px; top: 1133px;
    font-family: "Bebas Neue", sans-serif; font-size: 30px; line-height: 1; letter-spacing: 0.3px;
  }
</style>
</head>
<body>
<main class="flyer">
  <div class="backdrop" role="img" aria-label="Faded photo of a basketball player in action over a court"></div>

  <header class="masthead">
    <h1 class="masthead__title">Corporate Breakfast</h1>
    <div class="host">
      <span class="host__dot"></span>
      <div class="host__text">
        <div class="host__label">Hosted by</div>
        <div class="host__name">Wexford Lane</div>
      </div>
    </div>
  </header>

  <section class="speaker">
    <div class="speaker__with">With</div>
    <div class="speaker__name">Dylan<br>Morrow</div>
  </section>

  <section class="topic">
    <h2 class="topic__title">Leadership<br>&amp; Motivation</h2>
    <div class="topic__date">Thursday 22nd Sept 2016</div>
  </section>

  <div class="portrait" role="img" aria-label="Portrait photo of the speaker smiling"></div>

  <section class="panel panel--bio">
    <p>Dylan Morrow is a four-time Meridian Cup competitor, winning basketball player, coach, entrepreneur, motivational speaker, brand ambassador - and one of Australia's most recognized personalities and sporting figures.</p>
    <p>He was the first-ever Australian player to be signed to the PCX from the QVR and he also captained the Harbour Falcons to their first-ever title, helping to raise the profile of basketball around Australia. He has represented Australia at four Meridian Cup and played professionally for more than 20 years in Australia, Europe and the PCX. In February 2012 he was appointed Head Coach of the Harbour Falcons.</p>
  </section>

  <section class="panel panel--career">
    <p>Following his retirement from playing, Dylan earned a reputation as a successful entrepreneur and businessman. He built up a successful business in fast food franchising with more than 30 stores across six different brands which, at its peak in 2010, employed over 350 people. After his company was severely affected by the collapse of an KTE listed company in which he had purchased a 10-year contract, Dylan had to start all over again.</p>
    <p>Dylan has also held hosting, commentary and columnist roles with WMR, Vista Seven, Orbit Broadcast and Pike Athletics.</p>
  </section>

  <section class="schedule">
    <div class="schedule__slot" style="top:807px;height:71px;">7.30 am<br>Breakfast &amp; Networking</div>
    <div class="schedule__slot" style="top:890px;height:95px;">8.00 am<br>Dylan Morrow Talk<br>Leadership &amp; Motivation</div>
    <div class="schedule__slot" style="top:1002px;height:93px;">9.00 am<br>Business Card Draw<br>&amp; Finish</div>
  </section>

  <ul class="menu">
    <li>Mini croissants on arrival – Ham &amp; cheese, tomato &amp; cheese, plain</li>
    <li>Toast station – assorted sliced breads &amp; spreads</li>
    <li>Banana bread slice with honey ricotta</li>
    <li>Chicken &amp; herb chipolata</li>
    <li>Marinated lamb chops</li>
    <li>Creamy scrambled eggs with chives</li>
    <li>Mushroom &amp; cherry tomato kebabs</li>
    <li>Hash browns</li>
    <li>Assorted fruit cocktails with yoghurt &amp; granola, juice station</li>
    <li>Tea and coffee station included</li>
  </ul>

  <div class="venue-tag">Venue</div>
  <div class="venue-mark">
    <span class="venue-mark__dot"></span>
    <span class="venue-mark__name">Brindlemere Links Club</span>
  </div>
  <div class="address">Brindlemere Links Club, 17 Carrowvale St, Oatlands, NSW 2117</div>
</main>
</body>
</html>
```